Honey Labels for Manuka, Rewarewa, Multifloral and Manuka Blend honey

We require 4 label designs for our 4 types of honey i.e. Manuka, Rewarewa, Multifloral and Manuka Blend. Each design should be adapted for 250g, 500g, and 1kg PET jars. The design should look friendly and professional.

Tare: amber Square mason PET jars (see images attached)
Jar dimensions: see PDF attached

Target Market(s)

Worldwide. People caring for their health.

Industry/Entity Type

Health Product

Font styles to use
Serif
Decorative

Colors
6a429a
f37122
0692cd
9bcb3c

Requirements
Must have
• Each label should contain the following information
• • name of the honey e.g. Manuka Honey
• • VelloraTM logo (provided)
• • an image of a bird (provided),
• • nutrition table
• • a bar code
• • a place for a batch number and the best before date to be printed
• • volume: e.g. 250g, 500g, 1kg
• • Text: “Product of New Zealand”
• • Text: “Produced & packed by: Pemrick’s Hives Ltd. 48B Kolhurst Road, Tauranga 3162, New Zealand sales@vellorahoney.co.nz www.vellorahoney.co.nz
• • Ingredients: 100% Pure Raw New Zealand Honey
• • Text: “All specified values are averages.”
• • Not suitable for infants under 12 months. Do not use if cap seal is broken. Production methods involved with this product are not-GM. Contains bee products.
• • PET Recycling pictogram
• • Round corners
• Apart from different bird image each of 4 honey labels should have it's own color element e.g a different color background or a line.
• The birds:
• • Manuka honey: image of a Kingfisher bird
• o MGO Pictogram (80+, 100+, 200+, 300+ or 400+)
• • Rewarewa honey: image of a Kereru bird
• • Multifloral honey: image of a Tui bird
• • Manuka blend: image of a Pukekohe bird
Should not have
• Disclaimer: The provided images of birds is a copyright content. It is prohibited to use them outside of this project.

```html
<!DOCTYPE html>
<html lang="en">
<head>
<meta charset="utf-8">
<title>Vellora Rewarewa Honey Label</title>
<link rel="stylesheet" href="https://fonts.googleapis.com/css2?family=Cinzel:wght@500&family=Roboto:wght@700&display=swap">
<style>
  :root {
    --page: #ffffff;
    --purple: #6a429a;
    --purple-deep: #5a2f7e;
    --violet: #8a4a9e;
    --teal: #3f7d8c;
    --slate: #4b5f98;
    --lilac: #c6a9cf;
    --white: #ffffff;
    --logo-ink: #3c3a36;
  }
  * { margin: 0; padding: 0; box-sizing: border-box; }
  html, body {
    width: 1026px;
    height: 1200px;
    overflow: hidden;
    background: var(--page);
  }
  .canvas {
    position: relative;
    width: 1026px;
    height: 1200px;
  }
  .label {
    position: absolute;
    left: 53px;
    top: 130px;
    width: 920px;
    height: 940px;
    border-radius: 52px;
    overflow: hidden;
  }
  .label-pattern {
    position: absolute;
    inset: 0;
    background:
      linear-gradient(200deg, rgba(138,74,158,0.85) 0%, rgba(106,66,154,0) 45%),
      linear-gradient(330deg, rgba(75,95,152,0.9) 0%, rgba(75,95,152,0) 55%),
      linear-gradient(160deg, var(--slate) 0%, var(--teal) 38%, var(--purple-deep) 62%, var(--lilac) 100%);
  }
  .label-frame {
    position: absolute;
    inset: 30px;
    border: 3px solid var(--white);
    border-radius: 40px;
  }
  .name-band {
    position: absolute;
    left: 276px;
    top: 33px;
    width: 386px;
    height: 790px;
    background: var(--white);
  }
  .brand {
    position: absolute;
    left: 0;
    right: 0;
    top: 62px;
    display: flex;
    align-items: center;
    justify-content: center;
    gap: 14px;
  }
  .brand-dot {
    width: 18px;
    height: 18px;
    border-radius: 50%;
    background: var(--logo-ink);
  }
  .brand-name {
    font-family: "Cinzel", serif;
    font-weight: 500;
    font-size: 40px;
    letter-spacing: 3px;
    color: var(--logo-ink);
  }
  .product-name {
    position: absolute;
    left: 0;
    right: 0;
    top: 270px;
    text-align: center;
    font-family: "Roboto", sans-serif;
    font-weight: 700;
    font-size: 56px;
    line-height: 70px;
    color: var(--purple);
  }
  .bird-medallion {
    position: absolute;
    left: 298px;
    top: 465px;
    width: 344px;
    height: 344px;
  }
</style>
</head>
<body>
<main class="canvas">
  <section class="label">
    <div class="label-pattern" role="img" aria-label="Geometric honeycomb pattern in purple, violet and teal tones"></div>
    <div class="label-frame"></div>
    <div class="name-band">
      <div class="brand">
        <span class="brand-dot"></span>
        <span class="brand-name">VELLORA</span>
      </div>
      <h1 class="product-name">Rewarewa<br>honey</h1>
    </div>
    <svg class="bird-medallion" viewBox="0 0 344 344" role="img" aria-label="Polygonal illustration of a kereru bird in green, purple and white">
      <circle cx="172" cy="172" r="172" fill="#6a429a"/>
      <circle cx="172" cy="172" r="150" fill="none" stroke="#ffffff" stroke-width="3" stroke-dasharray="9 7"/>
      <circle cx="172" cy="172" r="120" fill="#7a5aa6" opacity="0.6"/>
    </svg>
  </section>
</main>
</body>
</html>
```